Spa Business Card Design Project

Hello! We are a boutique spa for men and women that is rebranding. I would like a memorable new business card that showcases our beautiful new logo and our unique business. I would like it to be classic/timeless and eclectic/artistic at the  same time.
I am a fan of negative space as you can tell from the logo. I am also open to any creative ideas.
Multi sided design. Two sided design is acceptable as an option, too. "Flaps/folds/whatever the design term is" are optional- whether full vertical or horizontal, half flap, full flap etc
On either side next to the golden snail I would potentially like to see "slow down. Enjoy Life."  Possibly on one statment on top of each other, crowned with the snail. Or the statment following the snail on one line... I am open for a creative suprise, too.
The back I would like room for the standard Information
"3187 Birch Lane
Ashbrook, New York 12405
(518) 462 3058
info@thecorvale spa.com
The snail is to be done in gold ink.
Can I also Have an option for cards that are individualized for staff members, too?

Updates
Reason: I apologize for the deadline extension. My day was more involved than anticipated in other matters. Hope to have this closed by next Tuesday.
Thank you

Target Market(s)
Men and women with expendable income between the ages of 30-55
Industry/Entity Type
Boutique
Requirements
Must have
- only black and gold ink.

Nice to have
- One of a kind.
Showcase the snail :-)
make you smile :-)
Fun, but professional.
Should not have
- Lots of color.
Too feminine.
Too busy.

```html
<!DOCTYPE html>
<html lang="en">
<head>
<meta charset="UTF-8">
<title>The Corvale Spa — Business Cards</title>
<link href="https://fonts.googleapis.com/css2?family=Lato:wght@300;400&display=swap" rel="stylesheet">
<style>
  :root {
    --gold: #d2aa68;
    --ink: #231f20;
    --paper: #ffffff;
    --stage: #ebe8e3;
    --muted: #3a3536;
    --rule: #c9c5c5;
  }
  * { box-sizing: border-box; margin: 0; padding: 0; }
  html, body { width: 1200px; height: 725px; overflow: hidden; }
  body {
    position: relative;
    background: var(--stage);
    font-family: "Lato", sans-serif;
    color: var(--ink);
  }
  .card {
    position: absolute;
    width: 508px;
    height: 289px;
    background: var(--paper);
    overflow: hidden;
    box-shadow: 0 2px 6px rgba(0,0,0,0.12);
  }
  .card--front   { left: 66px;  top: 55px; }
  .card--logo    { left: 621px; top: 55px; }
  .card--gold    { left: 71px;  top: 374px; background: var(--gold); }
  .card--white   { left: 632px; top: 381px; }

  /* front card */
  .brand {
    position: absolute;
    left: 36px; top: 64px;
    width: 210px;
    text-align: center;
  }
  .brand__name {
    font-weight: 400;
    font-size: 26px;
    line-height: 1.05;
    letter-spacing: 0.04em;
    text-transform: uppercase;
  }
  .brand__tagline {
    margin-top: 8px;
    font-size: 9.5px;
    font-weight: 400;
  }
  .divider {
    position: absolute;
    left: 268px; top: 62px;
    width: 1px; height: 92px;
    background: var(--rule);
  }
  .contact {
    position: absolute;
    left: 280px; top: 64px;
    list-style: none;
    font-size: 13.5px;
    font-weight: 400;
    color: var(--muted);
    line-height: 1.25;
  }
  .contact li { display: flex; align-items: flex-start; margin-bottom: 7px; }
  .contact svg { width: 11px; height: 11px; margin: 3px 7px 0 0; flex: none; }
  .wave { position: absolute; left: 0; top: 0; width: 508px; height: 289px; }
  .motto {
    position: absolute;
    left: 0; right: 0; bottom: 12px;
    text-align: center;
    color: var(--paper);
    font-size: 22px;
    font-weight: 300;
    letter-spacing: 0.09em;
  }

  /* logo card */
  .logo-card {
    position: absolute;
    inset: 0;
    display: flex;
    flex-direction: column;
    align-items: center;
    justify-content: center;
    padding-bottom: 16px;
  }
  .logo-card__name {
    font-size: 52px;
    font-weight: 400;
    line-height: 1.02;
    letter-spacing: 0.04em;
    text-transform: uppercase;
    text-align: center;
  }
  .logo-card__tagline {
    margin-top: 16px;
    font-size: 17px;
    font-weight: 400;
  }

  /* back cards */
  .mark {
    position: absolute;
    inset: 0;
    display: flex;
    align-items: center;
    justify-content: center;
    gap: 18px;
    font-size: 38px;
    font-weight: 400;
    letter-spacing: 0.05em;
    text-transform: uppercase;
  }
  .mark__dot { width: 30px; height: 30px; border-radius: 50%; flex: none; }
  .card--gold .mark { color: var(--paper); }
  .card--gold .mark__dot { background: var(--paper); }
  .card--white .mark { color: var(--gold); }
  .card--white .mark__dot { background: var(--gold); }
</style>
</head>
<body>

  <section class="card card--front" aria-label="Business card front">
    <svg class="wave" viewBox="0 0 508 289" aria-hidden="true">
      <path d="M0 196 C 90 236 170 250 260 230 C 360 208 440 186 508 190 L508 289 L0 289 Z" fill="var(--gold)"/>
      <path d="M0 194 C 70 232 150 246 240 232 C 340 214 430 180 508 187 L508 197 C 430 194 350 222 250 240 C 160 254 80 246 0 208 Z" fill="var(--ink)"/>
    </svg>

    <div class="brand">
      <p class="brand__name">The<br>Corvale Spa</p>
      <p class="brand__tagline">a boutique spa for Men &amp; Women</p>
    </div>

    <div class="divider"></div>

    <ul class="contact">
      <li>
        <svg viewBox="0 0 12 12" aria-hidden="true"><circle cx="6" cy="6" r="5.5" fill="none" stroke="var(--gold)"/><path d="M4 3.2 L5.2 3 L5.6 4.6 L4.9 5.1 C5.3 6 5.9 6.7 6.9 7.1 L7.4 6.4 L9 6.8 L8.8 8 C6.2 8.3 3.8 5.9 4 3.2 Z" fill="var(--gold)"/></svg>
        (518) 462 3058
      </li>
      <li>
        <svg viewBox="0 0 12 12" aria-hidden="true"><rect x="1" y="2.5" width="10" height="7" rx="1" fill="var(--gold)"/><path d="M1.5 3.2 L6 6.5 L10.5 3.2" fill="none" stroke="#fff" stroke-width="0.9"/></svg>
        info@thecorvalespa.com
      </li>
      <li>
        <svg viewBox="0 0 12 12" aria-hidden="true"><path d="M6 11.5 C3 7.8 2 6.2 2 4.6 A4 4 0 0 1 10 4.6 C10 6.2 9 7.8 6 11.5 Z" fill="var(--gold)"/><circle cx="6" cy="4.6" r="1.5" fill="#fff"/></svg>
        <span>3187 Birch Lane<br>Ashbrook, New York 12405</span>
      </li>
    </ul>

    <p class="motto">Slow down &amp; Enjoy Life.</p>
  </section>

  <section class="card card--logo" aria-label="Business card logo side">
    <div class="logo-card">
      <p class="logo-card__name">The<br>Corvale Spa</p>
      <p class="logo-card__tagline">a boutique spa for Men &amp; Women</p>
    </div>
  </section>

  <section class="card card--gold" aria-label="Business card back, gold">
    <div class="mark"><span class="mark__dot"></span>The Corvale Spa</div>
  </section>

  <section class="card card--white" aria-label="Business card back, white">
    <div class="mark"><span class="mark__dot"></span>The Corvale Spa</div>
  </section>

</body>
</html>
```